New Architectural Firm Business Cards

New Business card to compliment previous pixel forum logo (attached). Please design a business card that is simple, modern, creative....please do not use "symbols", simply the logo and associated graphics/text. The front should contain name/address/phone/email/web address (with graphics).....back should be 100% graphic design using the logo somehow. Hoping for a two color (black and yellow) design. full bleed design, no borders

Target Market(s)

Commercial Architecture Clients

Industry/Entity Type

Architecture

Contact Information for Business Card

Please design a business card that is simple, modern, creative....please do not use "symbols", simply the logo and associated graphics/text. The front should contain name/address/phone/email/web address (with graphics).....back should be 100% graphic design using the logo somehow

Font styles to use
Sans Serif

Colors
FFF300
FFF600
FEFA6F
FFFEC7
FFFEE8

Requirements
Must have
• Clean, Modern Design
Should not have
• Stock images or "icons"

```html
<!DOCTYPE html>
<html lang="en">
<head>
<meta charset="utf-8">
<title>Business Card – Front and Back</title>
<link rel="stylesheet" href="https://fonts.googleapis.com/css2?family=PT+Sans:wght@400;700&display=swap">
<style>
  :root {
    --canvas: #e6e6e6;
    --ink: #000000;
    --paper: #ffffff;
    --brand-yellow: #fff300;
    --font-main: "PT Sans", Tahoma, Verdana, sans-serif;
  }
  * { margin: 0; padding: 0; box-sizing: border-box; }
  html, body { width: 1054px; height: 1200px; overflow: hidden; background: var(--canvas); }
  body { font-family: var(--font-main); position: relative; }

  .card { position: absolute; left: 118px; width: 819px; height: 468px; overflow: hidden; }
  .card--front { top: 117px; background: var(--paper); }
  .card--back { top: 614px; background: var(--ink); }

  /* Front: dark contact panel */
  .contact-panel { position: absolute; left: 0; top: 0; width: 391px; height: 100%; background: var(--ink); }
  .divider-bar { position: absolute; left: 394px; top: 0; width: 15px; height: 100%; background: var(--ink); }

  .contact-list { list-style: none; }
  .contact-item { position: absolute; left: 0; width: 430px; height: 36px; }
  .contact-item:nth-child(1) { top: 140px; }
  .contact-item:nth-child(2) { top: 190px; }
  .contact-item:nth-child(3) { top: 243px; }
  .contact-item:nth-child(4) { top: 293px; }

  .contact-label {
    position: absolute; right: 93px; top: 0; line-height: 36px;
    font-size: 27px; color: var(--brand-yellow); white-space: nowrap;
  }
  .contact-pill {
    position: absolute; left: 350px; top: 0; width: 59px; height: 36px;
    background: var(--paper); border-radius: 18px 0 0 18px;
  }
  .contact-notch {
    position: absolute; left: 409px; top: 36px; width: 0; height: 0;
    border-top: 9px solid var(--ink); border-right: 7px solid transparent;
  }
  .contact-icon { position: absolute; left: 19px; top: 7px; width: 22px; height: 22px; }

  /* Front: identity */
  .identity { position: absolute; right: 28px; top: 16px; text-align: right; }
  .identity-name { font-size: 42px; font-weight: 700; color: var(--brand-yellow); line-height: 1.05; }
  .identity-title { font-size: 31px; font-weight: 400; color: var(--ink); line-height: 1.15; }

  .logo-badge {
    position: absolute; width: 146px; height: 146px; border-radius: 50%;
    display: flex; align-items: center; justify-content: center;
    font-size: 28px; white-space: nowrap;
  }
  .logo-badge--front { left: 643px; top: 292px; border: 2px solid var(--ink); color: var(--ink); }
  .logo-badge--back { left: 336px; top: 161px; border: 2px solid var(--paper); color: var(--brand-yellow); }

  /* Back */
  .accent-rule { position: absolute; left: 0; top: 408px; width: 504px; height: 3px; background: var(--brand-yellow); }
  .back-web { position: absolute; left: 518px; top: 391px; font-size: 28px; color: var(--paper); line-height: 36px; }
</style>
</head>
<body>

<section class="card card--front" aria-label="Card front">
  <div class="contact-panel"></div>
  <div class="divider-bar"></div>

  <ul class="contact-list">
    <li class="contact-item">
      <span class="contact-label">address</span>
      <span class="contact-pill">
        <svg class="contact-icon" viewBox="0 0 24 24" fill="none" stroke="#000" stroke-width="1.2">
          <path d="M12 22s-7-7.5-7-13a7 7 0 0 1 14 0c0 5.5-7 13-7 13z"/>
          <circle cx="12" cy="9" r="3"/>
        </svg>
      </span>
      <span class="contact-notch"></span>
    </li>
    <li class="contact-item">
      <span class="contact-label">phone</span>
      <span class="contact-pill">
        <svg class="contact-icon" viewBox="0 0 24 24" fill="none" stroke="#000" stroke-width="1.2">
          <path d="M5 3l4 0 2 5-2.5 1.5a11 11 0 0 0 6 6L16 13l5 2v4a2 2 0 0 1-2 2A17 17 0 0 1 3 5a2 2 0 0 1 2-2z"/>
        </svg>
      </span>
      <span class="contact-notch"></span>
    </li>
    <li class="contact-item">
      <span class="contact-label">e-mail</span>
      <span class="contact-pill">
        <svg class="contact-icon" viewBox="0 0 24 24" fill="none" stroke="#000" stroke-width="1.2">
          <rect x="2" y="6" width="20" height="12"/>
          <path d="M2 6l10 7 10-7M2 18l7-6M22 18l-7-6"/>
        </svg>
      </span>
      <span class="contact-notch"></span>
    </li>
    <li class="contact-item">
      <span class="contact-label">web address</span>
      <span class="contact-pill">
        <svg class="contact-icon" viewBox="0 0 24 24" fill="none" stroke="#000" stroke-width="1.2">
          <circle cx="12" cy="12" r="9"/>
          <ellipse cx="12" cy="12" rx="4" ry="9"/>
          <path d="M3 12h18M4.5 7.5h15M4.5 16.5h15"/>
        </svg>
      </span>
      <span class="contact-notch"></span>
    </li>
  </ul>

  <div class="identity">
    <h1 class="identity-name">Your Name</h1>
    <p class="identity-title">Your Title</p>
  </div>

  <div class="logo-badge logo-badge--front">Logo Here</div>
</section>

<section class="card card--back" aria-label="Card back">
  <div class="logo-badge logo-badge--back">Logo Here</div>
  <div class="accent-rule"></div>
  <p class="back-web">web address</p>
</section>

</body>
</html>
```